Flyer design for corporate telephone business

We are a new company called "Harbourline Voice" that sells complete tailored phone solutions to businesses in Australia. In most cases we can also save many businesses 50%+ off their monthly telephone bill. They also get to keep their existing telephone numbers. We also provide complete new set-up of business phone equipment and services. So I would like these 3 points highlighted and to stand out. We utilise the latest technology with advanced features. The flyer should be A5 sized. Single sided. White background with mainly a lot of blue. Also a mixture of grey, a little bit of black etc. The final design should make the potential customer want to call us to find out more info.
Target Market(s)
Business Owners, Managers, Decision makers
Industry/Entity Type
Telecommunications
Requirements
Must have
- Flyer must highlight the 3 x call to actions. Below is order of priority
- 1. We help businesses save 50%+ on their monthly phone bill
- 2. Keep your existing telephone numbers
- 3. Brand new phone installation services or upgrades.
- Also contact details
- sales@harbourlinevoice.com.au
- ph: 58170926
Nice to have
- I would like to try and include as many product images attached to this brief as possible without making the flyer look to busy. I would like the customer to know that we can supply phones, video conferencing, headsets, etc Our logo is currently being designed on another project. This should be finished shortly and I can add this to the brief once I have the finished design.

```html
<!DOCTYPE html>
<html lang="en">
<head>
<meta charset="utf-8">
<title>Harbourline Voice – Business Phone Solutions Flyer</title>
<link rel="stylesheet" href="https://fonts.googleapis.com/css2?family=PT+Sans+Narrow:wght@400;700&display=swap">
<style>
  :root {
    --ink: #231f20;
    --blue-deep: #1f8fc4;
    --blue-mid: #3aa9d8;
    --blue-soft: #8fcbe6;
    --blue-pale: #cfe8f4;
    --grey-mid: #9a9a9a;
    --grey-pale: #d9d9d9;
    --black: #1a1a1a;
    --paper: #ffffff;
  }
  * { box-sizing: border-box; margin: 0; padding: 0; }
  html, body { width: 852px; height: 1200px; overflow: hidden; background: var(--paper); }
  .flyer {
    position: relative;
    width: 852px;
    height: 1200px;
    overflow: hidden;
    background: var(--paper);
    font-family: "PT Sans Narrow", "Arial Narrow", sans-serif;
    color: var(--ink);
  }
  .backdrop {
    position: absolute;
    inset: 0;
    background:
      radial-gradient(ellipse at 50% 45%, rgba(255,255,255,0.55) 0%, rgba(255,255,255,0) 60%),
      linear-gradient(135deg, var(--paper) 0%, var(--blue-pale) 18%, var(--blue-soft) 38%, var(--blue-mid) 55%, var(--grey-pale) 70%, var(--blue-deep) 85%, var(--blue-soft) 100%);
  }
  .inner-frame {
    position: absolute;
    left: 52px; top: 52px;
    width: 742px; height: 840px;
    background: rgba(255,255,255,0.14);
  }
  .headline {
    position: absolute;
    top: 152px; left: 0; width: 100%;
    text-align: center;
    font-weight: 700;
    font-size: 56px;
    line-height: 82px;
    text-transform: uppercase;
    letter-spacing: -0.5px;
  }
  .benefits {
    position: absolute;
    left: 0; width: 100%;
    text-align: center;
    font-weight: 700;
    font-size: 44px;
    line-height: 32px;
    letter-spacing: -0.3px;
  }
  .benefit-save { top: 478px; }
  .benefit-numbers { top: 596px; }
  .benefit-install { top: 698px; }
  .contact {
    position: absolute;
    top: 855px; left: 0; width: 100%;
    text-align: center;
    font-weight: 400;
    font-size: 28px;
    line-height: 38px;
  }
  .product {
    position: absolute;
    border-radius: 18px;
  }
  .product-desk-phones {
    left: 14px; top: 940px; width: 300px; height: 250px;
    background: linear-gradient(180deg, #5b6066 0%, #2c2f33 60%, #1b1d20 100%);
  }
  .product-conference {
    left: 298px; top: 1000px; width: 236px; height: 170px;
    background: linear-gradient(160deg, #c9cdd1 0%, #7d8389 55%, #3a3e43 100%);
  }
  .product-cordless-touch {
    left: 540px; top: 1010px; width: 300px; height: 180px;
    background: linear-gradient(180deg, #4a4f55 0%, #25282c 70%, #17191b 100%);
  }
</style>
</head>
<body>
  <main class="flyer">
    <div class="backdrop" role="img" aria-label="Background of overlapping diamond tiles in blues, greys and black on white"></div>
    <div class="inner-frame"></div>

    <h1 class="headline">We solve<br>your communication<br>problems</h1>

    <p class="benefits benefit-save">We help businesses save 50%+<br>on their monthly phone bill</p>
    <p class="benefits benefit-numbers">Keep your existing telephone numbers</p>
    <p class="benefits benefit-install">Brand new phone installation services<br>or upgrades.</p>

    <p class="contact">sales@harbourlinevoice.com.au<br>ph: 58170926</p>

    <div class="product product-desk-phones" role="img" aria-label="Group of business desk phones and a cordless handset"></div>
    <div class="product product-conference" role="img" aria-label="Video conferencing camera, conference phone and base unit"></div>
    <div class="product product-cordless-touch" role="img" aria-label="Cordless phone with charging base and a colour touchscreen desk phone"></div>
  </main>
</body>
</html>
```